**** Web design project for BoltNet ****

For my ICT company BoltNet I need a website.

We design, build and host web-applications and we have our own CMS product. In the references part we want to show sample websites (thumbnails) + links.

It should look modern (WEB 2.0), rounded corners.

I want the following menu' s:
- Home
- Services
- References
- News
- About BoltNet
- Contact

Sample websites:
See attachments
http://www.vandoqa.com
http://www.greyfoxmanagement.nl

Reason: Want to take some time for feedback and improvements.

Reason: I'm waiting for a black background, with shadow and ambient light. You'll make a good chance!

Industry/Entity Type

It Company

Requirements
Must have
• - Fixed width (1024px), should fit on an IPad2
- Language selection English/Dutch
- Twitter/Facebook/LinkedIn/RSS icons
- Footer for Terms of use and Copyrights
- Search box
- 3 (or more) boxes for information i.e. news, blog or advertisements
Nice to have
• - Footer Site Map
- Contrasting background outside borders
- wide image (rotator) (with transperant sentence block)
- Shadow

```html
<!DOCTYPE html>
<html lang="en">
<head>
<meta charset="utf-8">
<title>BoltNet</title>
<link rel="stylesheet" href="https://fonts.googleapis.com/css2?family=Ubuntu:wght@400;500&family=Arimo:ital,wght@0,400;0,700;1,400&display=swap">
<style>
:root{
  --sky:#a9d4f2;
  --sky-light:#cfe8f9;
  --navy:#1c3a5c;
  --blue:#2e7fc2;
  --btn-top:#4d94d3;
  --btn-bottom:#1f64a8;
  --grey-band:#efefef;
  --text:#444;
  --muted:#666;
  --red:#c0282d;
  --green:#3a9a1c;
  --footer-top:#d9d9d9;
  --footer-bottom:#eeeeee;
  --bar:#a9a9a9;
  --white:#fff;
}
*{box-sizing:border-box;margin:0;padding:0}
html,body{width:697px;height:1200px;overflow:hidden}
body{position:relative;background:var(--white);font-family:"Arimo",Arial,sans-serif;color:var(--text)}
.abs{position:absolute}
.header{left:0;top:0;width:697px;height:341px;background:repeating-linear-gradient(135deg,var(--sky) 0 6px,#b3daf4 6px 12px)}
.logo{left:38px;top:34px;display:flex;align-items:center;gap:10px}
.logo-mark{width:54px;height:54px;border-radius:50%;background:var(--navy)}
.logo-name{font-family:"Ubuntu",sans-serif;font-size:30px;font-weight:400;color:#3e5566}
.nav{font-family:"Ubuntu",sans-serif;font-size:11.5px;letter-spacing:-.2px;color:var(--navy);top:47px;white-space:nowrap}
.nav.active{color:var(--white)}
.nav-line{left:309px;top:70px;width:358px;height:3px;background:var(--white)}
.lang{left:586px;top:96px;width:86px;height:15px;border:1px solid var(--navy);background:var(--sky-light);font-size:10px;padding-left:4px;line-height:13px}
.lang svg{position:absolute;right:4px;top:2px}
.content-band{left:0;top:341px;width:697px;height:208px;background:var(--grey-band)}
.hero{left:33px;top:116px;width:639px;height:264px;background:linear-gradient(120deg,#0b1a2e 0%,#163f6e 45%,#3cb2e8 75%,#0a2a4a 100%);box-shadow:0 10px 14px rgba(0,0,0,.35)}
.hero-caption{left:33px;top:132px;width:639px;height:45px;background:rgba(170,220,230,.55);font-size:16px;color:#1a2a3a;padding:13px 0 0 39px;letter-spacing:.2px}
.dots{left:561px;top:366px;display:flex;gap:5px}
.dots span{width:11px;height:11px;border-radius:50%;background:var(--white);border:2px solid #ccc}
.service{top:405px;width:196px}
.service-icon{position:absolute;left:0;top:0;width:34px;height:34px;border-radius:6px}
.service h3{margin-left:52px;font-size:12.5px;color:var(--blue);font-weight:700}
.service .sub{margin:5px 0 0 52px;font-size:7.5px;font-style:italic;color:#222}
.service hr{border:0;border-top:2px solid #ccc;margin-top:5px}
.service p.body{margin-top:11px;font-size:8.1px;line-height:12.4px;color:var(--muted)}
.btn{width:62px;height:21px;background:linear-gradient(var(--btn-top),var(--btn-bottom));color:var(--white);font-size:10px;text-align:center;line-height:21px;border-radius:2px}
.col-title{font-size:12px;font-weight:700;color:#111}
.col-sub{font-size:7.5px;font-style:italic;color:var(--blue)}
.avatar{width:45px;height:58px;border-radius:6px;background:linear-gradient(#9aa3ad,#2d3640)}
.quote{width:216px;height:54px;border:1px solid #ccc;border-radius:4px;font-size:7.4px;line-height:11px;padding:6px 8px;color:var(--muted);background:var(--white)}
.name{font-size:8px;color:var(--red)}
.name i{font-style:italic}
.divider{height:2px;background:#ddd}
.news-icon{width:44px;height:58px;border-radius:4px;background:linear-gradient(#c8d2dc,#5a6f84)}
.news-text{width:204px;font-size:7.4px;line-height:11px;color:var(--muted)}
.read-more{font-size:7.4px;color:var(--green)}
.works-title{left:29px;top:822px;font-size:12px;font-weight:700;color:#111}
.works-text{left:29px;top:848px;width:196px;font-size:8.1px;line-height:12.4px;color:var(--muted)}
.carousel{left:235px;top:813px;width:439px;height:109px;background:#f2f2f2;border-radius:4px;box-shadow:0 1px 3px rgba(0,0,0,.25)}
.thumb{top:829px;width:118px;height:73px;border:3px solid var(--white);box-shadow:0 0 2px rgba(0,0,0,.3)}
.footer{left:0;top:957px;width:697px;height:196px;background:linear-gradient(180deg,var(--footer-top),var(--footer-bottom) 40%,#d4d4d4)}
.about-title{left:43px;top:983px;font-size:10px;color:#555}
.about-text{left:43px;top:1013px;width:175px;font-size:7.4px;line-height:11px;color:var(--muted)}
.ad{left:256px;width:181px;height:69px;background:linear-gradient(#fafafa,#e8e8e8);border:1px solid #ccc;box-shadow:0 1px 3px rgba(0,0,0,.2);font-size:11px;color:#555;text-align:center;line-height:69px}
.newsletter{left:480px;top:984px;display:flex;align-items:center;gap:7px;font-size:9px;font-weight:700;color:#555}
.email{left:480px;top:1013px;width:181px;height:18px;background:#222;color:#888;font-size:8px;padding:4px 6px;border-radius:2px}
.subscribe{left:480px;top:1041px;width:55px;height:19px;background:var(--white);border:1px solid #777;border-radius:2px;font-size:8.5px;text-align:center;line-height:17px;color:#111}
.follow{left:491px;top:1101px;font-size:8.5px;color:#333}
.social{top:1096px;width:22px;height:22px;border-radius:50%}
.bottom-bar{left:0;top:1157px;width:697px;height:33px;background:var(--bar);color:var(--white);font-size:7.4px;line-height:33px}
.bottom-bar span{position:absolute;white-space:nowrap}
</style>
</head>
<body>
<header class="abs header"></header>
<div class="abs logo"><span class="logo-mark"></span><span class="logo-name">BoltNet</span></div>
<span class="abs nav active" style="left:315px">Home</span>
<span class="abs nav" style="left:364px">Services</span>
<span class="abs nav" style="left:421px">References</span>
<span class="abs nav" style="left:487px">News</span>
<span class="abs nav" style="left:534px">About BoltNet</span>
<span class="abs nav" style="left:624px">Contact</span>
<div class="abs nav-line"></div>
<svg class="abs" style="left:322px;top:72px" width="12" height="6" viewBox="0 0 12 6"><path d="M0 0h12L6 6z" fill="#fff"/></svg>
<div class="abs lang">Language<svg width="10" height="9" viewBox="0 0 10 9"><path d="M0 0h10L5 9z" fill="none" stroke="#1c3a5c"/></svg></div>

<div class="abs content-band"></div>
<div class="abs hero" role="img" aria-label="Photo of a hand touching glowing digital screen panels"></div>
<div class="abs hero-caption">LOREM IPSUM DOLOR SIT AMET, CONSECTETUR ADIPISICING ELIT,</div>
<div class="abs dots"><span></span><span></span><span></span><span></span><span></span></div>

<section class="abs service" style="left:40px">
  <span class="service-icon" style="background:#555;border-radius:50%"></span>
  <h3>Our Service1</h3><p class="sub">Lorem ipsum dolor sit amet</p><hr>
  <p class="body">Lorem ipsum dolor sit amet, consectetur adipisicing elit, sed do eiusmod tempor incididunt ut labore et dolore magna aliqua. Ut enim ad minim veniam, quis nostrud exercitation ullamco laboris nisi ut aliquip ex ea commodo consequat.</p>
</section>
<section class="abs service" style="left:259px">
  <span class="service-icon" style="background:#4b7fbf;width:24px;left:3px"></span>
  <h3>Our Service1</h3><p class="sub">Lorem ipsum dolor sit amet</p><hr>
  <p class="body">Lorem ipsum dolor sit amet, consectetur adipisicing elit, sed do eiusmod tempor incididunt ut labore et dolore magna aliqua. Ut enim ad minim veniam, quis nostrud exercitation ullamco laboris nisi ut aliquip ex ea commodo consequat.</p>
</section>
<section class="abs service" style="left:477px">
  <span class="service-icon" style="background:#d99a4c;width:40px"></span>
  <h3>Our Service1</h3><p class="sub">Lorem ipsum dolor sit amet</p><hr>
  <p class="body">Lorem ipsum dolor sit amet, consectetur adipisicing elit, sed do eiusmod tempor incididunt ut labore et dolore magna aliqua. Ut enim ad minim veniam, quis nostrud exercitation ullamco laboris nisi ut aliquip ex ea commodo consequat.</p>
</section>
<div class="abs btn" style="left:167px;top:510px">Learn More</div>
<div class="abs btn" style="left:387px;top:510px">Learn More</div>
<div class="abs btn" style="left:605px;top:510px">Learn More</div>

<div class="abs col-title" style="left:36px;top:566px">Blog</div>
<div class="abs col-sub" style="left:36px;top:583px">What Clients Say</div>
<div class="abs avatar" style="left:48px;top:604px" role="img" aria-label="Client avatar"></div>
<div class="abs quote" style="left:104px;top:606px">Lorem ipsum dolor sit amet, consectetur adipisicing elit, sed do eiusmod tempor incididunt ut labore et dolore magna aliqua. Ut enim ad minim veniam, quis nostrud exercitation ullamco laboris nisi ut aliquip ex ea commodo consequat.</div>
<div class="abs name" style="left:36px;top:670px"><i>Name</i> - Designation</div>
<div class="abs divider" style="left:36px;top:688px;width:291px"></div>
<div class="abs avatar" style="left:48px;top:701px" role="img" aria-label="Client avatar"></div>
<div class="abs quote" style="left:104px;top:703px">Lorem ipsum dolor sit amet, consectetur adipisicing elit, sed do eiusmod tempor incididunt ut labore et dolore magna aliqua. Ut enim ad minim veniam, quis nostrud exercitation ullamco laboris nisi ut aliquip ex ea commodo consequat.</div>
<div class="abs name" style="left:36px;top:767px"><i>Name</i> - Designation</div>

<div class="abs col-title" style="left:384px;top:566px">News</div>
<div class="abs col-sub" style="left:384px;top:583px">Latest Activities</div>
<div class="abs news-icon" style="left:392px;top:609px" role="img" aria-label="Clipboard with check mark icon"></div>
<div class="abs news-text" style="left:456px;top:614px">Lorem ipsum dolor sit amet, consectetur adipisicing elit, sed do eiusmod tempor incididunt ut labore et dolore magna aliqua. Ut enim ad minim veniam, quis nostrud exercitation ullamco laboris nisi ut aliquip ex ea commodo consequat.</div>
<div class="abs read-more" style="left:624px;top:658px">read more</div>
<div class="abs divider" style="left:374px;top:688px;width:295px"></div>
<div class="abs news-icon" style="left:392px;top:698px" role="img" aria-label="Clipboard with check mark icon"></div>
<div class="abs news-text" style="left:456px;top:703px">Lorem ipsum dolor sit amet, consectetur adipisicing elit, sed do eiusmod tempor incididunt ut labore et dolore magna aliqua. Ut enim ad minim veniam, quis nostrud exercitation ullamco laboris nisi ut aliquip ex ea commodo consequat.</div>
<div class="abs read-more" style="left:624px;top:747px">read more</div>

<div class="abs divider" style="left:15px;top:802px;width:667px;height:1px"></div>
<div class="abs works-title">Recent Works &amp; Products</div>
<div class="abs works-text">Lorem ipsum dolor sit amet, consectetur adipisicing elit, sed do eiusmod tempor incididunt ut labore et dolore magna aliqua. Ut enim ad minim veniam, quis nostrud exercitation ullamco laboris nisi ut aliquip ex ea commodo consequat.</div>
<div class="abs carousel"></div>
<svg class="abs" style="left:242px;top:859px" width="8" height="11" viewBox="0 0 8 11"><path d="M7 0L0 5.5 7 11z" fill="#111"/></svg>
<svg class="abs" style="left:658px;top:859px" width="8" height="11" viewBox="0 0 8 11"><path d="M1 0l7 5.5L1 11z" fill="#111"/></svg>
<div class="abs thumb" style="left:259px;background:linear-gradient(135deg,#0d2e6b,#3a78c8)" role="img" aria-label="Sample website thumbnail with blue data screens"></div>
<div class="abs thumb" style="left:394px;background:linear-gradient(#061a3a,#1a6fb0 70%,#04142c)" role="img" aria-label="Sample website thumbnail with server room"></div>
<div class="abs thumb" style="left:530px;background:linear-gradient(135deg,#5a9ec4,#b5dbe8)" role="img" aria-label="Sample website thumbnail with touch screen"></div>

<footer class="abs footer"></footer>
<div class="abs about-title">About Us</div>
<div class="abs about-text">Lorem ipsum dolor sit amet, consectetur adipisicing elit, sed do eiusmod tempor incididunt ut labore et dolore magna aliqua. Ut enim ad minim veniam, quis nostrud exercitation ullamco laboris nisi ut aliquip ex ea commodo consequat. Lorem ipsum dolor sit amet, consectetur adipisicing elit, sed do eiusmod tempor incididunt ut labore et dolore magna aliqua. Ut enim ad minim veniam, quis nostrud exercitation ullamco laboris nisi ut aliquip ex ea commodo conse-quat.</div>
<div class="abs ad" style="top:984px">Advertisement</div>
<div class="abs ad" style="top:1067px">Advertisement</div>
<div class="abs newsletter"><svg width="20" height="14" viewBox="0 0 20 14"><rect x=".5" y=".5" width="19" height="13" fill="#fff" stroke="#777"/><path d="M.5.5l9.5 7 9.5-7" fill="none" stroke="#777"/></svg>Newsletter Signup</div>
<div class="abs email">E-mail Address</div>
<div class="abs subscribe">Subscribe</div>
<div class="abs follow">Follow us On</div>
<span class="abs social" style="left:551px;background:#3a8fd0"></span>
<span class="abs social" style="left:581px;background:#2d5aa8"></span>
<span class="abs social" style="left:610px;background:#1f6fb0"></span>
<span class="abs social" style="left:637px;background:#e27a1f"></span>

<div class="abs bottom-bar">
  <span style="left:38px">Copyright Statement | Privacy policy</span>
  <span style="left:415px">Home</span>
  <span style="left:454px">Services</span>
  <span style="left:500px">References</span>
  <span style="left:550px">News</span>
  <span style="left:586px">About BoltNet</span>
  <span style="left:657px">Contact</span>
</div>
</body>
</html>
```